Whitcombe Framing Works - Card Design

I am looking to use the logo designs that you already did for me to develop a business card. I would like the card to have a black background and be double sided. I want white and green logo and text. I have attached an inspiration photo of a look that I like. I would like to use the Vertical Logo attached to take up the full front side of the card. On the back where I have my name and information, I would like to have the horizontal logo or maybe even just the image of the 'A' and trees without the text. I am open, but I am looking for something clean and simple and I want the green to really pop! Additional files can be found under Design #: 40593216

Target Market(s)

Homeowners

Industry/Entity Type

Construction

Contact Information for Business Card

Name: Marcus Pellow, Title: Project Manager, Phone: 831.555.0147, Email: whitcombeframingworks@mailbarn.net, address: 418 Juniper Ln, Felton, CA 95092, Lic# 2046318

Colors
00AB8E
00BBA5
67D7C9
C6EFE9
E9F9F6

Requirements
Nice to have
• I would like to see the logos that I have already got from SketchHarbor, though I am open to new ones

```html
<!DOCTYPE html>
<html lang="en">
<head>
<meta charset="utf-8">
<title>Whitcombe Framing Works – Business Card</title>
<link href="https://fonts.googleapis.com/css2?family=Montserrat:wght@400;600;700&display=swap" rel="stylesheet">
<style>
  :root {
    --backdrop: #2e2622;
    --card: #1c1c1c;
    --green: #6db544;
    --green-deep: #4f8f2c;
    --white: #ffffff;
    --soft-white: #e6e6e6;
    --emboss: #2b2b2b;
  }
  * { box-sizing: border-box; margin: 0; padding: 0; }
  html, body { width: 1200px; height: 716px; overflow: hidden; }
  body {
    background: var(--backdrop);
    font-family: "Montserrat", sans-serif;
    position: relative;
  }
  .card {
    position: absolute;
    top: 204px;
    width: 540px;
    height: 308px;
    background: var(--card);
    overflow: hidden;
    box-shadow: 0 14px 30px rgba(0,0,0,.45);
  }
  .card--back { left: 40px; }
  .card--front { left: 620px; }

  .brand-art { position: absolute; inset: 0; width: 100%; height: 100%; }

  .wordmark {
    position: absolute;
    left: 34px;
    top: 30px;
    font-weight: 700;
    font-size: 22px;
    letter-spacing: 1px;
    line-height: 1.1;
    text-transform: uppercase;
    color: var(--white);
    width: 300px;
  }

  .contact { position: absolute; left: 34px; top: 104px; color: var(--soft-white); }
  .contact__name {
    position: relative;
    padding-left: 14px;
    font-weight: 700;
    font-size: 17px;
    letter-spacing: .5px;
    text-transform: uppercase;
    color: var(--green);
  }
  .contact__name::before {
    content: "";
    position: absolute;
    left: 0; top: 1px;
    width: 6px; height: 18px;
    background: var(--green);
  }
  .contact__title { padding-left: 14px; font-size: 11px; margin-top: 2px; }
  .contact__licence { font-size: 11px; color: var(--green); margin-top: 12px; }
  .contact__address { font-size: 11px; line-height: 1.35; margin-top: 2px; }
  .contact__line {
    display: flex; align-items: center; gap: 7px;
    font-size: 11px; margin-top: 10px;
  }
  .contact__line + .contact__line { margin-top: 6px; }
  .contact__line svg { width: 10px; height: 10px; fill: var(--green); flex: none; }

  .front-name {
    position: absolute;
    right: 40px;
    top: 128px;
    font-weight: 700;
    font-size: 26px;
    letter-spacing: 1px;
    text-transform: uppercase;
    color: var(--emboss);
    text-align: right;
    line-height: 1.1;
    width: 240px;
  }
</style>
</head>
<body>

  <section class="card card--back">
    <svg class="brand-art" viewBox="0 0 540 308" role="img" aria-label="Large brand artwork of green trees and a white mark">
      <defs>
        <linearGradient id="artGradBack" x1="0" y1="1" x2="1" y2="0">
          <stop offset="0" stop-color="var(--green-deep)"/>
          <stop offset="1" stop-color="var(--green)"/>
        </linearGradient>
      </defs>
      <polygon points="190,308 540,120 540,308" fill="url(#artGradBack)"/>
    </svg>

    <div class="wordmark">Whitcombe Framing Works</div>

    <div class="contact">
      <div class="contact__name">Marcus Pellow</div>
      <div class="contact__title">Project Manager</div>
      <div class="contact__licence">Lic# 2046318</div>
      <div class="contact__address">418 Juniper Ln, Felton<br>CA 95092</div>
      <div class="contact__line">
        <svg viewBox="0 0 10 10" aria-hidden="true"><path d="M2 0h2l1 3-1.5 1a6 6 0 0 0 2.5 2.5L7 5l3 1v2a2 2 0 0 1-2 2A8 8 0 0 1 0 2a2 2 0 0 1 2-2z"/></svg>
        <span>831.555.0147</span>
      </div>
      <div class="contact__line">
        <svg viewBox="0 0 10 10" aria-hidden="true"><path d="M0 2h10v6H0z M0 2l5 3.5L10 2" /></svg>
        <span>whitcombeframingworks@mailbarn.net</span>
      </div>
    </div>
  </section>

  <section class="card card--front">
    <svg class="brand-art" viewBox="0 0 540 308" role="img" aria-label="Large brand artwork of a white mark beside green trees">
      <defs>
        <linearGradient id="artGradFront" x1="0" y1="0" x2="1" y2="1">
          <stop offset="0" stop-color="var(--green)"/>
          <stop offset="1" stop-color="var(--green-deep)"/>
        </linearGradient>
      </defs>
      <polygon points="0,0 250,0 250,308 0,230" fill="url(#artGradFront)"/>
    </svg>

    <div class="front-name">Whitcombe Framing Works</div>
  </section>

</body>
</html>
```